marcel's mobile mechanic

a business card that will get attention from clients
- name of the business: M'S MOBILE MECHANIC
- we currently do not have a logo and do not need one at the moment, happy for the designers to just put the business name on the card using appropriate fonts

Target Market(s)

low cost mobile repairs

Industry/Entity Type

Business

Contact Information for Business Card

attracts customers

Font styles to use
Sans Serif

Colors
0255a3
fbee3d
000000

Requirements
Must have
• (555) 318-4907
• Marcel Treviño
• for lower income target market
Nice to have
• "we save you money"
• Easy to read
Should not have
• nothing comes to mind

```html
<!DOCTYPE html>
<html lang="en">
<head>
<meta charset="utf-8">
<title>M'S Mobile Mechanic — Business Card</title>
<link href="https://fonts.googleapis.com/css2?family=Montserrat:wght@400;500;700&display=swap" rel="stylesheet">
<style>
  :root {
    --brand-blue: #0255a3;
    --brand-yellow: #fbee3d;
    --ink-white: #ffffff;
    --backdrop: #dcdcdc;
    --pattern-tone: #0a4f96;
  }
  * { box-sizing: border-box; margin: 0; padding: 0; }
  html, body {
    width: 1200px;
    height: 1200px;
    overflow: hidden;
    background: var(--backdrop);
    font-family: "Montserrat", sans-serif;
  }
  .canvas {
    position: relative;
    width: 1200px;
    height: 1200px;
  }
  .card {
    position: absolute;
    width: 756px;
    height: 432px;
    overflow: hidden;
  }
  /* Front side */
  .card--front {
    left: 350px;
    top: 138px;
    background: var(--ink-white);
  }
  .front__title-area {
    position: absolute;
    inset: 0 0 auto 0;
    height: 236px;
    display: flex;
    align-items: center;
    justify-content: center;
    padding-bottom: 30px;
  }
  .business-name {
    color: var(--brand-blue);
    font-weight: 700;
    font-size: 29px;
    letter-spacing: 0.2px;
  }
  .front__contact-band {
    position: absolute;
    left: 0;
    right: 0;
    top: 236px;
    bottom: 0;
    background: var(--brand-blue);
  }
  .band-notch {
    position: absolute;
    left: 50%;
    top: -1px;
    transform: translateX(-50%);
    width: 32px;
    height: 28px;
  }
  .contact-name {
    position: absolute;
    left: 0;
    right: 0;
    top: 44px;
    text-align: center;
    color: var(--brand-yellow);
    font-weight: 400;
    font-size: 26px;
  }
  .phone-icon {
    position: absolute;
    left: 50%;
    top: 84px;
    transform: translateX(-50%);
    width: 18px;
    height: 18px;
  }
  .phone-number {
    position: absolute;
    left: 0;
    right: 0;
    top: 110px;
    text-align: center;
    color: var(--ink-white);
    font-weight: 400;
    font-size: 20px;
    letter-spacing: 0.8px;
  }
  /* Back side */
  .card--back {
    left: 95px;
    top: 630px;
    background: var(--brand-blue);
  }
  .tool-pattern {
    position: absolute;
    inset: 0;
    background: var(--brand-blue);
  }
  .tagline {
    position: absolute;
    left: 0;
    right: 0;
    top: 196px;
    text-align: center;
    color: var(--ink-white);
    font-weight: 500;
    font-size: 32px;
    letter-spacing: 0.3px;
  }
</style>
</head>
<body>
<main class="canvas">
  <section class="card card--front" aria-label="Business card front">
    <div class="front__title-area">
      <h1 class="business-name">M'S MOBILE MECHANIC</h1>
    </div>
    <div class="front__contact-band">
      <svg class="band-notch" viewBox="0 0 32 28" aria-hidden="true">
        <polygon points="0,0 32,0 16,28" fill="#ffffff"/>
      </svg>
      <p class="contact-name">Marcel Treviño</p>
      <svg class="phone-icon" viewBox="0 0 24 24" aria-hidden="true">
        <path fill="#ffffff" d="M6.6 10.8c1.4 2.8 3.8 5.1 6.6 6.6l2.2-2.2c.3-.3.7-.4 1-.2 1.1.4 2.3.6 3.6.6.6 0 1 .4 1 1V20c0 .6-.4 1-1 1C10.6 21 3 13.4 3 4c0-.6.4-1 1-1h3.5c.6 0 1 .4 1 1 0 1.3.2 2.5.6 3.6.1.3 0 .7-.2 1z"/>
      </svg>
      <p class="phone-number">(555) 318-4907</p>
    </div>
  </section>

  <section class="card card--back" aria-label="Business card back">
    <div class="tool-pattern" role="img" aria-label="Scattered pattern of darker blue mechanic tool icons: wrenches, screwdrivers, gears, hex nuts and mobile phones"></div>
    <p class="tagline">WE SAVE YOU MONEY</p>
  </section>
</main>
</body>
</html>
```